Envoys Trophy - Mexico (Cricket)

This year The Halvern Bat League is hosting a tournament called the Envoys Trophy, on March 22nd at our Club (Quintal Sporting Club) in Mexico City

4 teams lead by the respective Ambassadors (GB, Australia, India and Mexico) will compete for a Cup in the twenty/20 format of the game of cricket

We want as many people to come as possible hence need a flyer to put on the websites of the various embassies plus other societies like The Corlan Fellowship, PELORAN society (Southern Pacific Friends Circle Group etc)

We are also looking at sponsors who are interested in being involved with cricket due to its potential in Mexico, its brand value, as well as its links in countries such as India – for example the biggest cinema group here (Vistarama) is opening cinemas in India and would like to be involved. Brevik Motorworks is now an Indian company etc.

So if you could come up with something that looks professional, and attracts the interest of sponsors and spectators that would be great – the event will also attract the interest of the media, and will be followed by our Garden Gala, which is also something for which we will need a flyer.

The tournament's first game is at 11.am
Refreshments will be available
Sponsors will also be showcasing their products
Kids welcome
Address - Quintal Sporting Club, Santa Clara de Mizquitlan, Cerro Pinto, Mexico

Target Market(s)

The flyer aims to attract the interest of spectators (families) from the various communities involved (British, Australian, Indian and Mexican) for a high end event that we will look to repeat every year.
We also want to attract the interest of sponsors of high end brands who want to be associated with the event.

Industry/Entity Type

Club

Requirements
Must have
• Logo of Halvern Bat League

```html
<!DOCTYPE html>
<html lang="en">
<head>
<meta charset="utf-8">
<title>Envoys Trophy Tournament</title>
<link href="https://fonts.googleapis.com/css2?family=Open+Sans:wght@400;600;700;800&family=Montserrat:wght@600;700&display=swap" rel="stylesheet">
<style>
  :root {
    --green: #4b8f36;
    --orange: #ef7f1a;
    --orange-dark: #d96a10;
    --blue: #2f5bbf;
    --tan: #cd8c57;
    --slate: #6477a6;
    --ink: #3b3b3b;
    --ink-soft: #555;
    --white: #fff;
    --rule: #9a9a9a;
  }
  * { margin: 0; padding: 0; box-sizing: border-box; }
  html, body { width: 1200px; height: 720px; overflow: hidden; background: var(--white); }
  .flyer {
    position: relative; width: 1200px; height: 720px; overflow: hidden;
    font-family: "Open Sans", Arial, sans-serif; color: var(--ink); background: var(--white);
  }
  .presenter-bar {
    position: absolute; left: 0; top: 0; width: 600px; height: 79px; background: var(--green);
    color: var(--white); font-size: 29px; font-weight: 600; letter-spacing: -0.8px;
    padding: 21px 0 0 36px;
  }
  .trophy-icon { position: absolute; left: 56px; top: 131px; width: 114px; height: 113px; }
  .event-title {
    position: absolute; left: 180px; top: 134px; width: 360px; text-align: center;
    color: var(--orange); font-weight: 800; font-size: 42px; line-height: 41px; letter-spacing: -1.5px;
    text-transform: uppercase;
  }
  .event-date {
    position: absolute; left: 180px; top: 223px; width: 360px; text-align: center;
    color: var(--orange-dark); font-weight: 700; font-size: 15.5px; letter-spacing: -0.6px;
  }
  .teams { position: absolute; left: 0; top: 298px; width: 602px; height: 104px; display: flex; }
  .team {
    width: 150.5px; height: 104px; position: relative; color: var(--white);
    font-size: 16.5px; font-weight: 600; letter-spacing: -0.6px; text-align: center;
  }
  .team--mexico { background: var(--green); }
  .team--britain { background: var(--blue); }
  .team--india { background: var(--tan); }
  .team--australia { background: var(--slate); }
  .team-flag { position: absolute; left: 37px; top: 19px; width: 76px; height: 44px; }
  .team-name { position: absolute; left: 0; right: 0; top: 72px; }
  .photo { position: absolute; }
  .photo--batsman { left: 600px; top: 0; width: 271px; height: 402px; }
  .photo--ball { left: 871px; top: 0; width: 329px; height: 299px; }
  .photo--gear { left: 871px; top: 299px; width: 329px; height: 103px; }
  .club-mark {
    position: absolute; left: 964px; top: 34px; display: flex; align-items: center; gap: 10px;
    color: var(--white); font-weight: 700; font-size: 16px; line-height: 16px; letter-spacing: -0.5px;
  }
  .club-mark-dot { width: 44px; height: 44px; border-radius: 50%; background: var(--white); opacity: .9; }
  .headline {
    position: absolute; left: 0; top: 420px; width: 1200px; text-align: center;
    font-size: 35px; font-weight: 400; letter-spacing: -0.5px; color: var(--ink);
  }
  .headline strong { font-weight: 700; }
  .double-rule { position: absolute; left: 0; top: 479px; width: 1200px; height: 5px;
    border-top: 1px solid var(--rule); border-bottom: 1px solid var(--rule); }
  .doors-panel {
    position: absolute; left: 19px; top: 493px; width: 569px; height: 135px; background: var(--green);
    color: var(--white); padding: 28px 0 0 25px;
  }
  .doors-time { font-family: "Montserrat", Arial, sans-serif; font-weight: 700; font-size: 42px; line-height: 50px; letter-spacing: 0.5px; }
  .doors-notes { margin-top: 10px; font-size: 14.5px; font-weight: 700; }
  .web-links {
    position: absolute; right: 29px; top: 508px; text-align: right; list-style: none;
    font-size: 18.5px; font-weight: 700; line-height: 26.5px; color: var(--ink);
  }
  .footer-rule { position: absolute; left: 0; top: 640px; width: 1200px; height: 1px; background: var(--green); }
  .sponsors { position: absolute; left: 29px; top: 656px; height: 50px; display: flex; align-items: center; gap: 26px;
    font-size: 17px; font-weight: 700; color: var(--ink); letter-spacing: -0.3px; }
  .sponsor { display: flex; align-items: center; gap: 8px; }
  .sponsor-square { width: 16px; height: 16px; background: var(--blue); }
  .sponsor-circle { width: 18px; height: 18px; border-radius: 50%; background: var(--green); }
  .venue-address {
    position: absolute; right: 22px; top: 662px; font-style: normal;
    font-size: 13px; font-weight: 700; line-height: 13.5px; color: var(--ink-soft);
  }
</style>
</head>
<body>
<main class="flyer">
  <header class="presenter-bar">The Halvern Bat League Presents:</header>

  <svg class="trophy-icon" role="img" aria-label="Gold trophy cup icon" viewBox="0 0 114 113">
    <defs><linearGradient id="gold" x1="0" y1="0" x2="0" y2="1">
      <stop offset="0" stop-color="#f3e04e"/><stop offset="1" stop-color="#f5a623"/></linearGradient></defs>
    <rect width="114" height="113" rx="8" fill="url(#gold)"/>
  </svg>

  <h1 class="event-title">Envoys Trophy<br>Tournament</h1>
  <p class="event-date">MARCH 22, AT QUINTAL SPORTING CLUB</p>

  <section class="teams">
    <div class="team team--mexico">
      <svg class="team-flag" role="img" aria-label="Flag of Mexico" viewBox="0 0 76 44">
        <defs><linearGradient id="mx" x1="0" y1="0" x2="1" y2="0"><stop offset="0" stop-color="#1f7a3a"/><stop offset=".5" stop-color="#f4f4f4"/><stop offset="1" stop-color="#c8202f"/></linearGradient></defs>
        <rect width="76" height="44" fill="url(#mx)"/></svg>
      <span class="team-name">MEXICO</span>
    </div>
    <div class="team team--britain">
      <svg class="team-flag" role="img" aria-label="Flag of Great Britain" viewBox="0 0 76 44"><rect width="76" height="44" fill="#8a3350"/></svg>
      <span class="team-name">GREAT BRITAIN</span>
    </div>
    <div class="team team--india">
      <svg class="team-flag" role="img" aria-label="Flag of India" viewBox="0 0 76 44">
        <defs><linearGradient id="in" x1="0" y1="0" x2="0" y2="1"><stop offset="0" stop-color="#f39a33"/><stop offset=".5" stop-color="#f6f6f6"/><stop offset="1" stop-color="#2e8b2e"/></linearGradient></defs>
        <rect width="76" height="44" fill="url(#in)"/></svg>
      <span class="team-name">INDIA</span>
    </div>
    <div class="team team--australia">
      <svg class="team-flag" role="img" aria-label="Flag of Australia" viewBox="0 0 76 44"><rect width="76" height="44" fill="#1d2f7a"/></svg>
      <span class="team-name">AUSTRALIA</span>
    </div>
  </section>

  <svg class="photo photo--batsman" role="img" aria-label="Photo of a cricket batsman in whites playing a shot in front of the stumps" viewBox="0 0 271 402" preserveAspectRatio="none">
    <defs><linearGradient id="bat" x1="0" y1="0" x2="0" y2="1"><stop offset="0" stop-color="#35501c"/><stop offset=".45" stop-color="#c9c3a2"/><stop offset=".7" stop-color="#a9ad83"/><stop offset="1" stop-color="#6f8a3a"/></linearGradient></defs>
    <rect width="271" height="402" fill="url(#bat)"/>
  </svg>
  <svg class="photo photo--ball" role="img" aria-label="Photo of a red leather cricket ball resting on grass" viewBox="0 0 329 299" preserveAspectRatio="none">
    <defs><linearGradient id="ball" x1="0" y1="0" x2="0" y2="1"><stop offset="0" stop-color="#8fa05a"/><stop offset=".55" stop-color="#8a3a2c"/><stop offset="1" stop-color="#5f7a30"/></linearGradient></defs>
    <rect width="329" height="299" fill="url(#ball)"/>
  </svg>
  <svg class="photo photo--gear" role="img" aria-label="Photo of cricket pads, gloves, bat and balls on grass" viewBox="0 0 329 103" preserveAspectRatio="none">
    <defs><linearGradient id="gear" x1="0" y1="0" x2="0" y2="1"><stop offset="0" stop-color="#7f9a45"/><stop offset="1" stop-color="#5c7a2c"/></linearGradient></defs>
    <rect width="329" height="103" fill="url(#gear)"/>
  </svg>
  <div class="club-mark"><span class="club-mark-dot"></span><span>The Quintal<br>Sporting Club</span></div>

  <h2 class="headline">4 TEAMS COMPETE AT <strong>THE PRESTIGIOUS QUINTAL SPORTING CLUB</strong></h2>
  <div class="double-rule"></div>

  <section class="doors-panel">
    <p class="doors-time">DOORS OPEN AT 11AM</p>
    <p class="doors-notes">Refreshments will be available * Kids welcome * Garden Gala Games</p>
  </section>

  <ul class="web-links">
    <li>www.envoystrophy.org</li>
    <li>www.envoystrophy.org</li>
    <li>www.quintalsporting.org</li>
    <li>www.envoystrophy.org</li>
  </ul>

  <div class="footer-rule"></div>
  <footer class="sponsors">
    <span class="sponsor"><span class="sponsor-square"></span>Vistarama</span>
    <span class="sponsor">Brevik Motorworks</span>
    <span class="sponsor"><span class="sponsor-circle"></span>Halvern Bat League</span>
  </footer>
  <address class="venue-address">Quintal Sporting Club,<br>Santa Clara de Mizquitlan,<br>Cerro Pinto, Mexico</address>
</main>
</body>
</html>
```